plumbers buisness card

A buisness card for a plumbing buisness
needs to have a water theme with navy blue, light blue and white
with an image of either a water drop, pipes, tools or something relating to plumbing and incorperating my buisness name as a logo

"Kesterly Plumbing" is the words that need to stand out with "& gasfitting" to be smaller
Updates

spelling error on brief, "maintenance"
and also could you include my email m_kesterly@mailnest.com.au

Industry/Entity Type

Plumbing

Contact Information for Business Card

Kesterly Plumbing & Gasfitting

marcus kesterly
0493612085

specialising in
-new homes
-maitenance
-renovations

license no.
-73804

```html
<!DOCTYPE html>
<html lang="en">
<head>
<meta charset="utf-8">
<title>Kesterly Plumbing &amp; Gasfitting – Business Card</title>
<link rel="stylesheet" href="https://fonts.googleapis.com/css2?family=Open+Sans:wght@400;600;700&display=swap">
<style>
  :root {
    --stage: #5f5b59;
    --teal: #3cb2c3;
    --ink: #333333;
    --white: #ffffff;
    --paper-light: #ffffff;
    --paper-shade: #dedede;
  }
  * { margin: 0; padding: 0; box-sizing: border-box; }
  html, body {
    width: 1200px; height: 416px; overflow: hidden;
    background: var(--stage);
    font-family: "Open Sans", sans-serif;
  }
  .stage { position: relative; width: 1200px; height: 416px; }
  .side-label {
    position: absolute; color: var(--white);
    font-size: 28px; font-weight: 400; letter-spacing: 0.5px;
  }
  .side-label--front { left: 242px; top: 18px; }
  .side-label--back { left: 812px; top: 12px; }

  .card {
    position: absolute; top: 75px; width: 525px; height: 300px; overflow: hidden;
  }
  .card--front {
    left: 45px;
    background: linear-gradient(100deg, var(--paper-shade) 0%, var(--paper-light) 40%, var(--paper-light) 55%, var(--paper-shade) 100%);
  }
  .card--back { left: 633px; background: var(--teal); }
  .card svg.card__shape { position: absolute; left: 0; top: 0; }

  .card__art {
    position: absolute; left: 310px; top: 105px; width: 230px; height: 200px;
    background: radial-gradient(ellipse at 55% 40%, rgba(190,190,190,0.45), rgba(210,210,210,0) 70%);
  }

  .front-text {
    position: absolute; left: 150px; width: 350px; top: 0;
    text-align: center; color: var(--ink);
  }
  .brand-name { font-weight: 700; font-size: 30px; line-height: 1; }
  .front-text .brand-name { margin-top: 30px; }
  .brand-tagline { font-size: 17px; line-height: 1; margin-top: 5px; }
  .contact-name { font-weight: 700; font-size: 14px; margin-top: 41px; line-height: 18px; }
  .contact-line { font-size: 13px; line-height: 18px; }
  .services-title { font-weight: 700; font-size: 13.5px; margin-top: 33px; line-height: 18px; }
  .services-list { font-size: 13px; line-height: 18px; }
  .footer-line { font-size: 13px; margin-top: 22px; line-height: 18px; }
  .footer-line strong { font-weight: 700; }

  .back-text {
    position: absolute; left: 185px; width: 310px; top: 122px;
    text-align: center; color: var(--white);
  }
  .back-text .brand-name { font-size: 28px; }
  .back-text .brand-tagline { font-size: 16px; margin-top: 6px; }
</style>
</head>
<body>
<div class="stage">
  <div class="side-label side-label--front">Front</div>
  <div class="side-label side-label--back">Back</div>

  <section class="card card--front">
    <svg class="card__shape" width="525" height="300" viewBox="0 0 525 300" aria-hidden="true">
      <polygon points="0,0 150,107 75,153 150,200 0,300" fill="var(--teal)"/>
      <circle cx="40" cy="150" r="33" fill="var(--white)"/>
    </svg>
    <div class="card__art" role="img" aria-label="Faint tap illustration in the background"></div>
    <div class="front-text">
      <div class="brand-name">Kesterly Plumbing</div>
      <div class="brand-tagline">&amp; Gasfitting</div>
      <div class="contact-name">Marcus Kesterly</div>
      <div class="contact-line">Cell : 0493612085</div>
      <div class="services-title">Specialising in :</div>
      <div class="services-list">New homes - Maintenance - Renovations</div>
      <div class="footer-line"><strong>email :</strong> m_kesterly@mailnest.com.au | license no. 73804</div>
    </div>
  </section>

  <section class="card card--back">
    <svg class="card__shape" width="525" height="300" viewBox="0 0 525 300" aria-hidden="true">
      <defs>
        <radialGradient id="back-wedge" cx="0.2" cy="0.5" r="0.9">
          <stop offset="0" stop-color="#ffffff"/>
          <stop offset="1" stop-color="#d4d4d4"/>
        </radialGradient>
      </defs>
      <polygon points="0,0 150,107 75,153 150,200 0,300" fill="url(#back-wedge)"/>
      <circle cx="41" cy="152" r="33" fill="var(--white)"/>
    </svg>
    <div class="back-text">
      <div class="brand-name">Kesterly Plumbing</div>
      <div class="brand-tagline">&amp; Gasfitting</div>
    </div>
  </section>
</div>
</body>
</html>
```